2nd Opinion Radiology web page

Looking for a web page design for second opinion radiology service. Main page will have a link directing user to locate CD on their computer/device, and will take contents of CD and upload to server, which I will specify.

Web page needs a form to enter user's name, contact info, and create a log in for user. User must click to accept terms of service, which will be a paragraph which i will provide. User will log back in, after uploading cd, to find report, which will be able to be viewed once user pays, by coinvera. User will need to be able to download report.

There will be a small paragraph explaining what we do: Provide expert second opinions, worldwide. We provide interpretations from radiologists with many years of experience and training from the world's best institutions, including brennick and corvalen regional hospital.

A second paragraph: Have questions or doubts about your CT or MRI? Get a second opinion from experts at ScanPerch. Tap into the full potential of your images.

Thanks

Reason: The website does not need to be fully coded, however, should include graphics and design so a web designer can simply take the design, images, and objects and code the site.

People who are unsure of their medical care and looking for a second opinion.

Training

```html
<!DOCTYPE html>
<html lang="en">
<head>
<meta charset="utf-8">
<title>ScanPerch — Expert 2nd Opinions</title>
<link rel="stylesheet" href="https://fonts.googleapis.com/css2?family=PT+Sans:wght@400;700&family=Comfortaa:wght@700&display=swap">
<style>
  :root {
    --brand-blue: #215a78;
    --brand-blue-dark: #1b4d68;
    --accent-lime: #a9b60f;
    --accent-lime-dark: #8e9a08;
    --text-grey: #666;
    --tagline-grey: #7a7a7a;
    --field-bg: #f2f2f2;
    --field-border: #e0e0e0;
    --rule-grey: #c8c8c8;
    --white: #fff;
  }
  * { box-sizing: border-box; margin: 0; padding: 0; }
  html, body { width: 1200px; height: 1096px; overflow: hidden; background: var(--white); }
  body { position: relative; font-family: Arial, Helvetica, sans-serif; color: var(--text-grey); }

  .brand { position: absolute; left: 27px; top: 34px; display: flex; align-items: center; gap: 14px; }
  .brand-mark { width: 40px; height: 40px; background: var(--brand-blue); border-radius: 6px; }
  .brand-name { font-family: "PT Sans", sans-serif; font-weight: 700; font-size: 44px; color: var(--brand-blue); letter-spacing: 1px; }

  .tagline { position: absolute; left: 381px; top: 42px; font-family: "PT Sans", sans-serif; font-size: 29px; color: var(--tagline-grey); letter-spacing: .5px; }
  .tagline strong { font-weight: 700; }

  .main-nav { position: absolute; left: 0; top: 122px; }
  .main-nav a { position: absolute; top: 0; font-family: "Comfortaa", sans-serif; font-weight: 700; font-size: 19px; color: var(--brand-blue); text-decoration: none; white-space: nowrap; letter-spacing: .5px; }
  .main-nav .is-active::after { content: ""; position: absolute; left: 50%; bottom: -14px; transform: translateX(-50%); border: 7px solid transparent; border-bottom-color: var(--accent-lime); }

  .account-tabs a { position: absolute; top: 115px; height: 44px; border-radius: 10px 10px 0 0; background: var(--brand-blue); color: var(--white); font-family: "Comfortaa", sans-serif; font-weight: 700; font-size: 15px; text-decoration: none; display: flex; align-items: center; justify-content: center; }

  .header-rule { position: absolute; left: 0; top: 158px; width: 1200px; height: 4px; background: var(--brand-blue); }

  .hero { position: absolute; left: 0; top: 162px; width: 1200px; height: 540px;
    background: linear-gradient(100deg, #e9ddc9 0%, #f3ede3 30%, #f6f4f1 50%, #e4e7ea 75%, #d4d9dd 100%); }

  .signup-card { position: absolute; left: 83px; top: 230px; width: 385px; height: 361px; background: var(--white); border-radius: 18px; box-shadow: 0 0 0 3px rgba(255,255,255,.6), 0 2px 8px rgba(0,0,0,.12); }
  .signup-card h2 { position: absolute; left: 28px; top: 24px; font-family: "PT Sans", sans-serif; font-weight: 700; font-size: 29px; color: var(--brand-blue); }
  .field { position: absolute; left: 36px; width: 306px; height: 38px; border-radius: 19px; background: var(--field-bg); border: 1px solid var(--field-border); padding-left: 24px; display: flex; align-items: center; font-size: 15px; font-weight: 700; color: #555; }
  .terms { position: absolute; left: 46px; top: 234px; display: flex; align-items: center; gap: 8px; font-size: 13px; color: #555; }
  .terms .radio { width: 14px; height: 14px; border-radius: 50%; border: 1px solid #999; background: linear-gradient(#fff, #ddd); }
  .terms a { color: var(--brand-blue); text-decoration: underline; }
  .btn-signup { position: absolute; left: 43px; top: 273px; width: 118px; height: 37px; border-radius: 3px; background: linear-gradient(var(--accent-lime), var(--accent-lime-dark)); color: var(--white); font-size: 15px; font-weight: 700; display: flex; align-items: center; justify-content: center; letter-spacing: .5px; }

  .about { position: absolute; left: 39px; top: 734px; width: 1130px; }
  .about h1 { font-family: "PT Sans", sans-serif; font-weight: 400; font-size: 37px; color: var(--brand-blue); letter-spacing: .5px; }
  .about p { font-size: 19.5px; line-height: 25px; margin-top: 18px; }
  .about p + p { margin-top: 23px; }
  .about .question { color: var(--accent-lime); }
  .about .cta { color: var(--brand-blue); }

  .footer-rule { position: absolute; left: 0; top: 1007px; width: 1200px; height: 1px; background: var(--rule-grey); }
  .footer-nav { position: absolute; left: 36px; top: 1028px; font-size: 15px; color: var(--brand-blue); }
  .footer-nav a { color: var(--brand-blue); text-decoration: none; }
  .copyright { position: absolute; left: 34px; top: 1055px; font-size: 13px; color: #888; }
</style>
</head>
<body>
  <header>
    <div class="brand"><span class="brand-mark"></span><span class="brand-name">SCANPERCH</span></div>
    <p class="tagline">PROVIDING EXPERT <strong>2ND OPINIONS</strong> WORLD WIDE</p>
    <nav class="main-nav">
      <a class="is-active" style="left:27px">HOME</a>
      <a style="left:147px">WHY US</a>
      <a style="left:288px">WHO WE ARE</a>
      <a style="left:476px">CONTACT US</a>
    </nav>
    <nav class="account-tabs">
      <a style="left:991px;width:91px">SIGN IN</a>
      <a style="left:1086px;width:92px">SIGN UP</a>
    </nav>
    <div class="header-rule"></div>
  </header>

  <section class="hero" role="img" aria-label="Photo of a nurse in white scrubs smiling at a patient lying on a CT scanner table"></section>

  <form class="signup-card">
    <h2>Create Account</h2>
    <div class="field" style="top:71px">name</div>
    <div class="field" style="top:123px">email address</div>
    <div class="field" style="top:174px">contact number</div>
    <label class="terms"><span class="radio"></span>I agree to the <a>Terms of Service</a></label>
    <div class="btn-signup">SIGN UP</div>
  </form>

  <main class="about">
    <h1>WHAT WE DO</h1>
    <p>Provide expert second opinions, worldwide. We provide interpretations from radiologists with many years of experience and training from the world's best institutions, including brennick and corvalen regional hospital.</p>
    <p><span class="question">Have questions or doubts about your CT or MRI?</span> <span class="cta">Get a second opinion from experts at ScanPerch</span>. Tap into the full potential of your images.</p>
  </main>

  <footer>
    <div class="footer-rule"></div>
    <nav class="footer-nav"><a>Home</a> · <a>Why us</a> · <a>Who we are</a> · <a>Contact Us</a> · <a>Terms of Use</a></nav>
    <p class="copyright">© Copyright 2013 ScanPerch. All rights reserved.</p>
  </footer>
</body>
</html>
```